Word Page Templates x 5

1 x Letterhead Template with Header and Footer able to be printed to paper and pdf with non blurry resolution
- File attached looks ok on computer screen but does not print the same
- We are wanting it to print like it looks on the screen
- We are wanting it to print not fuzzy in resolution
- We are wanting the banner to be on the absolute edge of the page like it is on the computer screen
- We are needing to print this to paper and pdf with perfect resolution and colour

Please can someone help us!!

I have provided the logo files in our posession. If better resolutions are required please let us know.

We are also wanting 4 simple page templates to be setup in Landscape and Portrait orientation as well once we are happy with the letterhead that is provided samples have been provided
Updates

Hi all I have the vector files available now along with a Colour profile

Requirements
Must have
• Clear when printed on A4 Paper
Should not have
• Blurry images, Colour must be correct (same as Logo) - Please reference our website if need be ..... vornal.com.au

```html
<!DOCTYPE html>
<html lang="en">
<head>
<meta charset="utf-8">
<title>Vornal Pavement Services – Letterhead</title>
<link rel="stylesheet" href="https://fonts.googleapis.com/css2?family=Montserrat:wght@600;700;800&display=swap">
<style>
  :root {
    --brand-green: #1b8a4c;
    --brand-blue: #1f3f88;
    --band-mid: #177a78;
    --ink-grey: #8a8d92;
    --badge-grey: #d9dbde;
    --canvas-bg: #ffffff;
    --page-edge: #d6d6d6;
  }
  * { margin: 0; padding: 0; box-sizing: border-box; }
  html, body {
    width: 1200px; height: 1200px; overflow: hidden;
    background: var(--canvas-bg);
    font-family: "Montserrat", Arial, sans-serif;
  }
  .letterhead {
    position: absolute; left: 269px; top: 130px;
    width: 663px; height: 938px;
    background: #fff;
    box-shadow: 0 0 0 3px var(--page-edge);
    overflow: hidden;
  }
  .edge-band {
    position: absolute; left: 0; width: 100%;
    background: linear-gradient(90deg, var(--brand-green) 0%, var(--band-mid) 50%, var(--brand-blue) 100%);
  }
  .edge-band--top { top: 0; height: 32px; }
  .edge-band--bottom { bottom: 0; height: 31px; }

  .wordmark {
    position: absolute;
    color: var(--brand-blue);
    font-weight: 800;
    letter-spacing: 1px;
    line-height: 1;
  }
  .wordmark--header { left: 46px; top: 62px; font-size: 50px; }
  .wordmark--footer { left: 497px; top: 860px; font-size: 27px; }

  .contact-list {
    position: absolute; left: 436px; top: 58px;
    list-style: none;
    font-size: 10.5px; font-weight: 700;
    color: var(--brand-blue);
    line-height: 16px;
  }
  .contact-list .label {
    display: inline-block; width: 20px;
    color: var(--brand-green);
  }

  .rule { position: absolute; top: 815px; height: 3px; }
  .rule--blue { left: 38px; width: 422px; background: var(--brand-blue); }
  .rule--green { left: 488px; width: 131px; background: var(--brand-green); }

  .affiliation-title {
    position: absolute; left: 47px; top: 829px;
    font-size: 9.5px; font-weight: 700;
    color: var(--brand-blue);
    letter-spacing: 0.2px;
  }
  .affiliate-badge {
    position: absolute; top: 852px; height: 42px;
    background: var(--badge-grey);
    border-radius: 4px;
  }
  .affiliate-badge--one { left: 46px; width: 112px; background: #c9d2e4; }
  .affiliate-badge--two { left: 173px; width: 62px; }
  .affiliate-badge--three { left: 253px; width: 42px; border-radius: 50%; }
  .affiliate-badge--four { left: 311px; width: 50px; }
</style>
</head>
<body>
  <main class="letterhead">
    <div class="edge-band edge-band--top" role="img" aria-label="Chevron pattern band in green to blue"></div>

    <header>
      <div class="wordmark wordmark--header">VORNAL</div>
      <ul class="contact-list">
        <li><span class="label">A.</span>PO Box 2318, Coralvale QLD 4290</li>
        <li><span class="label">P.</span>07 5500 1234</li>
        <li><span class="label">E.</span>admin@vornal.com.au</li>
        <li><span class="label">W.</span>www.vornal.com.au</li>
      </ul>
    </header>

    <footer>
      <div class="rule rule--blue"></div>
      <div class="rule rule--green"></div>
      <p class="affiliation-title">VORNAL PAVEMENT SERVICES ARE PROUDLY AFFILIATED WITH</p>
      <div class="affiliate-badge affiliate-badge--one" role="img" aria-label="Affiliate badge"></div>
      <div class="affiliate-badge affiliate-badge--two" role="img" aria-label="Affiliate badge"></div>
      <div class="affiliate-badge affiliate-badge--three" role="img" aria-label="Member badge"></div>
      <div class="affiliate-badge affiliate-badge--four" role="img" aria-label="Association badge"></div>
      <div class="wordmark wordmark--footer">VORNAL</div>
    </footer>

    <div class="edge-band edge-band--bottom" role="img" aria-label="Chevron pattern band in green to blue"></div>
  </main>
</body>
</html>
```